Brisa Home Residential cleaning services- Opening Flyer

1. I would like to have flyer design offering the hourly rate residential cleaning normal rate will be 35 AED per hour.
2. I want to have a special opening rate which is less than 25 AED which is equivalent to 30% Off.This opening offer will be limited time
We have a different cleaning packages like "Basic , Deep, And custom"
3. Also we have different types contracts Yearly/Monthly/Weekly and daily.
4. we are providing cleaning material and cleaning equipment upon request.And all the material used are environmental friendly.
5. Our customers mostly will be house wives.
6. Our service will be available in Ruwais city.
7. I would like to have a modern attractive flyer, i like it to be smart in its colors and the psychology of the customers.
8. I like to have attractive statements like " Now Available in Ruwais" and other statements from your own.
9. I will attach my logo design and if you need any other uploads let me know.
10. Our slogan is "Experience the Difference"
11. Paper size , i expect to be A5 (210mm x 148mm).
12. I am expecting the flyer to be single size as it will translated to another language in the other side.
13. please use the statement also ( less than 25 AED)
14. Do the arrangement you can see to the flyer statements as to look professional and comfortable to read.
15. Company web site is " www.brisahome.ae"
16. company email " support@brisahome.ae"
17. I will update you with contact number soon
18. My contacts are
Support@brisahome.ae
+971 508817394
+971 508817396
19. Update some slogans to be used
Industry/Entity Type
Residential
Look and feel
Each slider illustrates characteristics of the customer's brand and the style your logo design should communicate.

```html
<!DOCTYPE html>
<html lang="en">
<head>
<meta charset="utf-8">
<title>Brisa Home – Opening Flyer</title>
<link rel="stylesheet" href="https://fonts.googleapis.com/css2?family=Roboto+Condensed:wght@400;700&family=Berkshire+Swash&display=swap">
<style>
  :root{
    --navy:#2c4f9e;
    --navy-dark:#1f3a7a;
    --magenta:#b5338f;
    --purple-band:#b0368f;
    --orange:#f07f3c;
    --cyan:#1fb0e6;
    --green:#7bbf4a;
    --lime:#8dc63f;
    --yellow:#fde428;
    --ink:#262626;
    --script:#555555;
    --strike:#e0262b;
    --white:#ffffff;
  }
  *{margin:0;padding:0;box-sizing:border-box}
  html,body{width:847px;height:1200px;overflow:hidden;background:var(--white)}
  .flyer{position:relative;width:847px;height:1200px;overflow:hidden;background:var(--white);
    font-family:"Roboto Condensed",Arial,sans-serif;color:var(--ink)}

  .brand{position:absolute;left:34px;top:70px;display:flex;align-items:center;gap:18px}
  .brand-dot{width:70px;height:70px;border-radius:50%;background:var(--green)}
  .brand-name{font-weight:700;font-size:62px;color:var(--navy);line-height:1}

  .offer-percent{position:absolute;left:52px;top:222px;font-size:86px;font-weight:700;color:var(--navy);letter-spacing:-1px;line-height:1}
  .offer-old{position:absolute;left:53px;top:318px;font-size:38px;font-weight:700;color:var(--ink);line-height:1}
  .offer-old svg{position:absolute;left:36px;top:-10px}
  .offer-new{position:absolute;left:368px;top:230px;font-size:64px;font-weight:700;color:var(--magenta);line-height:1.05}

  .packages-band{position:absolute;left:0;top:419px}
  .packages-title{position:absolute;left:28px;top:430px;font-size:32px;font-weight:700;color:var(--white);line-height:1.12}
  .package-tags{position:absolute;left:24px;top:524px;display:flex;gap:6px}
  .package-tag{position:relative;width:132px;height:55px;color:var(--white);font-size:28px;font-weight:700;
    display:flex;align-items:center;justify-content:center}
  .package-tag::before{content:"";position:absolute;left:0;right:0;top:5px;bottom:5px;
    border-top:1px dashed rgba(255,255,255,.85);border-bottom:1px dashed rgba(255,255,255,.85)}
  .package-tag.basic{background:var(--orange)}
  .package-tag.deep{background:var(--cyan)}
  .package-tag.custom{background:var(--green)}

  .tagline{position:absolute;left:26px;top:648px;font-family:"Berkshire Swash",Georgia,serif;font-size:40px;
    color:var(--script);line-height:1.3}
  .tagline span{display:block}
  .tagline span:last-child{padding-left:10px}

  .hero-photo{position:absolute;left:350px;top:392px;width:440px;height:529px;
    background:radial-gradient(ellipse at 55% 45%,#f3d6c0 0%,#f6c9b8 28%,#f4b36a 55%,rgba(255,255,255,0) 78%)}

  .info-strip{position:absolute;left:0;top:921px;width:847px;height:46px;display:flex}
  .info-ruwais{width:328px;background:var(--lime);display:flex;align-items:center;gap:12px;padding-left:26px}
  .info-eco{flex:1;background:var(--navy);display:flex;align-items:center;gap:12px;padding-left:22px}
  .info-strip p{color:var(--white);font-size:21px;font-weight:700}

  .contracts{position:absolute;left:0;top:967px;width:847px;height:138px;background:var(--navy)}
  .contracts-title{position:absolute;left:26px;top:32px;font-size:30px;font-weight:700;color:var(--white);line-height:1.3;text-align:center}
  .contract-plan{position:absolute;top:14px;width:110px;height:110px;border-radius:50%;
    display:flex;flex-direction:column;align-items:center;justify-content:center;color:var(--navy-dark);font-weight:700}
  .contract-plan::before{content:"";position:absolute;inset:6px;border-radius:50%;border:2px dashed rgba(255,255,255,.9)}
  .contract-plan .plan-name{font-size:23px;line-height:1.1}
  .contract-plan .plan-price{font-size:28px;line-height:1.1}
  .plan-yearly{left:275px;background:#c8539c}
  .plan-monthly{left:402px;background:var(--orange)}
  .plan-weekly{left:525px;background:var(--cyan)}
  .plan-daily{left:652px;background:var(--green)}

  .contact-footer{position:absolute;left:0;top:1105px;width:847px;height:95px;background:var(--yellow)}
  .contact-note{position:absolute;left:14px;top:32px;width:210px;text-align:center;font-size:14px;font-weight:700;color:var(--navy-dark);line-height:1.3}
  .contact-phones{position:absolute;left:273px;top:10px;font-size:32px;font-weight:700;color:var(--navy-dark)}
  .contact-web{position:absolute;left:222px;top:52px;font-size:32px;font-weight:700;color:var(--navy-dark)}
</style>
</head>
<body>
<div class="flyer">

  <div class="brand">
    <div class="brand-name">Brisa Home</div>
    <div class="brand-dot"></div>
  </div>

  <div class="offer-percent">30% Off.</div>
  <div class="offer-old">35 AED per hour
    <svg width="250" height="58" viewBox="0 0 250 58"><line x1="2" y1="6" x2="248" y2="54" stroke="var(--strike)" stroke-width="3"/><line x1="2" y1="54" x2="248" y2="6" stroke="var(--strike)" stroke-width="3"/></svg>
  </div>
  <div class="offer-new">Now 25 AED<br>per hour.</div>

  <div class="hero-photo" role="img" aria-label="Smiling housekeeper in apron and yellow gloves holding a broom and a bucket of cleaning products"></div>

  <svg class="packages-band" width="535" height="93" viewBox="0 0 535 93"><polygon points="0,0 535,0 442,93 0,93" fill="var(--purple-band)"/></svg>
  <div class="packages-title">We have a different cleaning<br>packages like</div>
  <div class="package-tags">
    <div class="package-tag basic">Basic</div>
    <div class="package-tag deep">Deep</div>
    <div class="package-tag custom">Custom</div>
  </div>

  <div class="tagline"><span>Trusted, Reliable,</span><span>Professional</span><span>Maid Service.</span></div>

  <div class="info-strip">
    <div class="info-ruwais">
      <svg width="32" height="32" viewBox="0 0 32 32"><circle cx="16" cy="16" r="16" fill="var(--navy)"/><path d="M16 7a6 6 0 0 0-6 6c0 4.5 6 12 6 12s6-7.5 6-12a6 6 0 0 0-6-6zm0 8.5a2.5 2.5 0 1 1 0-5 2.5 2.5 0 0 1 0 5z" fill="var(--white)"/></svg>
      <p>Now Available in Ruwais</p>
    </div>
    <div class="info-eco">
      <svg width="32" height="32" viewBox="0 0 32 32"><circle cx="16" cy="16" r="16" fill="var(--lime)"/><path d="M16 25V14M16 18c-5 0-7-4-7-8 4 0 7 3 7 8zm0 0c4 0 7-3 7-7-4 0-7 3-7 7z" fill="var(--white)" stroke="var(--white)" stroke-width="1.2"/></svg>
      <p>Our Products are environmental friendly.</p>
    </div>
  </div>

  <div class="contracts">
    <div class="contracts-title">We have different<br>types contracts</div>
    <div class="contract-plan plan-yearly"><span class="plan-name">Yearly</span><span class="plan-price">$-00</span></div>
    <div class="contract-plan plan-monthly"><span class="plan-name">Monthly</span><span class="plan-price">$-00</span></div>
    <div class="contract-plan plan-weekly"><span class="plan-name">Weekly</span><span class="plan-price">$-00</span></div>
    <div class="contract-plan plan-daily"><span class="plan-name">Daily</span><span class="plan-price">$-00</span></div>
  </div>

  <div class="contact-footer">
    <div class="contact-note">Contact us Today to Schedule<br>your house cleaning.</div>
    <div class="contact-phones">+971 508817394 / +971 508817396</div>
    <div class="contact-web">support@brisahome.ae |&nbsp; www.brisahome.ae</div>
  </div>

</div>
</body>
</html>
```